Foot and ankle surgeon requires a website design

I need a website where prospective and established patients can obtain information and then direct them to making appointments. My practice is a highly professional surgical practice specialising in surgery to the foot and ankle. My title is Mr Colin Dwyer, Podiatric Foot & Ankle Surgeon. My qualifications are: BSc MSc FACPS
The practice website will require information on: Locations, phone numbers to make appointments, general background on podiatric surgery,
I would like to include information on: my hospital appointments, surgical fellowships held, training programs undertaken, association memberships, publications written, links to useful websites
A page dedicated to common foot conditions would be useful and also a page with referral information including an online registration section that will be sent direct to the receptionist.
Examples of similar websites include:
http://www.trevorkeplinfeet.com.au/
http://www.vollardfootsurgeon.com.au/
I will provide files on logo, self photos and my personal training history etc.
Also if there is going to be a background theme I personally am associated with surfing and beach activities, it would be great if this was able to be reflected in the design.
Thank you.

```html
<!DOCTYPE html>
<html lang="en">
<head>
<meta charset="utf-8">
<title>Mr Colin Dwyer – Podiatric Foot &amp; Ankle Surgeon</title>
<link rel="stylesheet" href="https://fonts.googleapis.com/css2?family=Lato:wght@400;700&display=swap">
<style>
:root{
  --teal:#3b7c8e;
  --teal-dark:#2f6878;
  --navy:#16406f;
  --footer:#0e3f78;
  --orange:#f26a1f;
  --text:#333;
  --muted:#666;
  --grey-band:#f1f1f1;
  --line:#d6d6d6;
  --white:#fff;
}
*{box-sizing:border-box;margin:0;padding:0}
html,body{width:800px;height:1200px;overflow:hidden}
body{position:relative;background:var(--white);font-family:'Lato',sans-serif;color:var(--text)}
.abs{position:absolute}

/* top navigation */
.topnav{position:absolute;left:0;top:0;width:800px;height:38px;
  background:repeating-linear-gradient(90deg,var(--teal) 0 2px,var(--teal-dark) 2px 3px)}
.topnav a{position:absolute;top:12px;color:var(--white);font-size:12px;text-decoration:none;line-height:14px;white-space:nowrap}
.topnav .sep{position:absolute;top:13px;width:1px;height:13px;background:rgba(255,255,255,.8)}
.topnav .active{top:4px;left:120px;width:62px;height:34px;background:linear-gradient(#fff,#ececec);
  color:#222;text-align:center;padding-top:9px;border-radius:2px 2px 0 0}

/* header */
.brand{left:96px;top:81px;display:flex;align-items:center;gap:7px}
.brand-dot{width:16px;height:16px;border-radius:50%;background:var(--orange)}
.brand-name{font-size:11px;color:var(--navy);font-weight:400}
.brand-sub{left:121px;top:97px;font-size:5.5px;color:var(--navy);line-height:8px}
.phone-icon{left:442px;top:68px;width:36px;height:36px;border:2px solid #d9d9d9;border-radius:50%;
  display:flex;align-items:center;justify-content:center;background:#fff}
.phone-num{left:487px;top:76px;font-size:16px;letter-spacing:1px;color:var(--navy)}
.search{left:612px;top:79px;width:100px;height:15px;border-radius:8px;background:#e6e6e6;
  box-shadow:inset 0 1px 2px rgba(0,0,0,.15);font-size:7px;color:#888;padding:3px 0 0 7px}
.search svg{position:absolute;right:5px;top:3px}

/* slider */
.slider{left:88px;top:134px;width:624px;height:266px;border:1px solid var(--line);border-radius:3px;background:#fff}
.slide-photo{left:115px;top:148px;width:298px;height:197px;
  background:linear-gradient(100deg,#f4f4f4 0 25%,#c9d8e6 40%,#c7a56a 70%,#b99258)}
.slide-title{left:430px;top:156px;font-size:21px;color:var(--navy);font-weight:400;white-space:nowrap}
.slide-text{left:431px;top:191px;font-size:8.2px;line-height:16px;color:var(--muted);white-space:nowrap}
.btn{left:504px;top:292px;width:80px;height:26px;background:var(--orange);color:#fff;font-size:11px;
  text-align:center;line-height:26px;border:1px solid #e3e3e3;box-shadow:0 0 0 1px #f6b48c}
.slide-rule{left:107px;top:363px;width:586px;height:2px;background:#e5e5e5}
.dots{left:360px;top:377px;display:flex;gap:4px}
.dots span{width:8px;height:8px;border-radius:50%;border:1px solid #bbb;background:#f3f3f3}
.dots span.on{background:#444;box-shadow:inset 0 0 0 2px #f3f3f3}

/* feature cards */
.card-frame{width:173px;height:112px;border:1px solid #bdbdbd;background:#e9e9e9;padding:3px;top:444px}
.card-frame div{width:100%;height:100%}
.card-title{top:562px;font-size:14px;color:var(--navy);font-weight:400}
.card-text{top:583px;font-size:8.6px;line-height:11.6px;color:#333;white-space:nowrap}

/* welcome band */
.band{left:0;top:662px;width:800px;height:430px;background:var(--grey-band);border-top:1px solid #ddd}
.welcome-title{left:90px;top:684px;font-size:32px;color:var(--orange);font-weight:400}
.welcome-text{left:90px;top:727px;font-size:11.2px;line-height:20px;color:#333;white-space:nowrap}
.panel{left:526px;width:186px;background:linear-gradient(#ededed,#e0e0e0);border:1px solid #d2d2d2}
.panel-title{position:absolute;font-size:14px;color:var(--orange);white-space:nowrap}
.news-text{position:absolute;left:14px;top:44px;font-size:9px;line-height:12px;color:#333;white-space:nowrap}
.news-text b{color:var(--navy);font-weight:700}
.appt{position:absolute;left:20px;display:flex;font-size:6px;line-height:9px;color:#444}
.appt .date{width:18px;text-align:right;padding-right:4px;border-right:2px solid var(--navy);margin-right:5px}

.col-title{top:940px;font-size:19px;color:var(--orange);font-weight:400}
.list{top:977px;font-size:11px;line-height:15.2px;list-style:none;color:#333}
.list li::before{content:"• "}
.gallery-main{left:362px;top:966px;width:106px;height:72px;border:1px solid #ccc;
  background:linear-gradient(120deg,#fff 0 30%,#e9d2c0 60%,#f1e1d5)}
.thumb{top:1045px;height:21px;border:1px solid #ccc}
.field{left:568px;width:144px;background:#e8e8e8;font-size:7px;font-style:italic;color:#888;padding:4px 8px}
.submit{left:570px;top:1058px;width:59px;height:16px;background:var(--orange);color:#fff;font-size:8px;line-height:16px;padding-left:8px}

/* footer */
.footer{left:0;top:1092px;width:800px;height:108px;background:var(--footer);color:#fff}
.footer a{position:absolute;top:31px;font-size:8.5px;font-weight:700;color:#fff;text-decoration:none}
.footer .sep{position:absolute;top:28px;width:1px;height:14px;background:rgba(255,255,255,.7)}
.copyright{position:absolute;left:88px;top:63px;font-size:7px;letter-spacing:-.2px}
.social{position:absolute;top:85px;width:11px;height:11px;border-radius:2px}
.address{position:absolute;right:88px;top:24px;text-align:right;font-size:8px;font-weight:700;line-height:16.8px;letter-spacing:.2px}
</style>
</head>
<body>

<nav class="topnav">
  <a class="active" href="#">Home</a>
  <a href="#" style="left:198px">Appointment</a>
  <span class="sep" style="left:285px"></span>
  <a href="#" style="left:306px">About</a>
  <span class="sep" style="left:354px"></span>
  <a href="#" style="left:371px">Services</a>
  <span class="sep" style="left:430px"></span>
  <a href="#" style="left:446px">Get In Touch</a>
</nav>

<header>
  <div class="abs brand"><span class="brand-dot"></span><span class="brand-name">Mr Colin Dwyer</span></div>
  <div class="abs brand-sub">M.Sc. B.Sc. F.A.C.P.S.<br>Podiatric Foot &amp; Ankle Surgeon</div>
  <div class="abs phone-icon">
    <svg width="18" height="20" viewBox="0 0 18 20"><path d="M4 1 L7 5 L5 7 C6 10 8 13 11 14 L13 12 L17 15 L15 19 C8 19 1 11 1 4 Z" fill="#f26a1f"/></svg>
  </div>
  <div class="abs phone-num">08 9000 1234</div>
  <div class="abs search">Search
    <svg width="10" height="10" viewBox="0 0 10 10"><circle cx="4" cy="4" r="3" fill="none" stroke="#777" stroke-width="1.4"/><path d="M6 6 L9 9" stroke="#777" stroke-width="1.6"/></svg>
  </div>
</header>

<section>
  <div class="abs slider"></div>
  <div class="abs slide-photo" role="img" aria-label="Surgeon in white coat and blue gloves examining a patient's foot"></div>
  <h1 class="abs slide-title">ABOUT FOOT SURGERY</h1>
  <p class="abs slide-text">Etiam dignissim lectus id diam varius egestas. Curabitur vel<br>libero massa. Phasellus scelerisque est ac enim interdum<br>pharetra. Nam tristique venenatis tortor non interdum. Aliquam<br>molestie sem eget ipsum dapibus congue. Cras venenatis nisi<br>nec est faucibus consequat.</p>
  <div class="abs btn">View Details</div>
  <div class="abs slide-rule"></div>
  <div class="abs dots"><span class="on"></span><span></span><span></span><span></span><span></span><span></span><span></span></div>
</section>

<section>
  <div class="abs card-frame" style="left:114px"><div role="img" aria-label="Doctor examining a patient's foot" style="background:linear-gradient(100deg,#f3f3f3 0 30%,#c6d4e2 45%,#c5a46c 75%)"></div></div>
  <div class="abs card-frame" style="left:314px"><div role="img" aria-label="Doctor testing a foot reflex" style="background:linear-gradient(90deg,#2f8f8f 0 45%,#f0ddd0 70%,#fafafa)"></div></div>
  <div class="abs card-frame" style="left:514px"><div role="img" aria-label="Close examination of a bare foot" style="background:linear-gradient(180deg,#bfc9d3,#e9e2dc 60%,#f3f3f3)"></div></div>

  <h2 class="abs card-title" style="left:117px">Lorem ipsum</h2>
  <h2 class="abs card-title" style="left:318px">Lorem ipsum</h2>
  <h2 class="abs card-title" style="left:518px">Lorem ipsum</h2>
  <p class="abs card-text" style="left:118px">Lorem ipsum is a dummy text only.<br>Dolor sit amet, consectetur adipiscing<br>elit. Nullam felis mauris, eleifend ac<br>rhoncus non.</p>
  <p class="abs card-text" style="left:318px">Lorem ipsum is a dummy text only.<br>Dolor sit amet, consectetur adipiscing<br>elit. Nullam felis mauris, eleifend ac<br>rhoncus non.</p>
  <p class="abs card-text" style="left:518px">Lorem ipsum is a dummy text only.<br>Dolor sit amet, consectetur adipiscing<br>elit. Nullam felis mauris, eleifend ac<br>rhoncus non.</p>
</section>

<section>
  <div class="abs band"></div>
  <h2 class="abs welcome-title">Welcome...</h2>
  <div class="abs welcome-text">
    <p>Lorem ipsum is a dummy text only. Dolor sit amet, consectetur adipiscing<br>elit. Nullam felis mauris, eleifend ac rhoncus non, lobortis at diam.<br>Pellentesque suscipit nulla sit amet venenatis porttitor. In augue felis.</p>
    <p style="margin-top:11px">Vestibulum bibendum, nulla quis viverra pharetra, lorem dolor<br>tincidunt turpis, ut fermentum velit ligula pretium mi.<br>Pellentesque euismod rutrum massa.</p>
  </div>

  <div class="abs panel" style="top:688px;height:94px">
    <svg class="abs" style="left:14px;top:6px" width="28" height="26" viewBox="0 0 28 26"><rect x="1" y="5" width="20" height="20" fill="none" stroke="#f26a1f" stroke-width="2"/><path d="M9 17 L23 3 L26 6 L12 20 L8 21 Z" fill="#f26a1f"/></svg>
    <div class="panel-title" style="left:49px;top:12px">Recent News</div>
    <p class="news-text">Praesent venenatis nec ligula in<br>tincidunt. Suspendisse fringilla<br>odio non. &nbsp;<b>Read more... &gt;&gt;</b></p>
  </div>

  <div class="abs panel" style="top:790px;height:94px">
    <svg class="abs" style="left:14px;top:7px" width="24" height="24" viewBox="0 0 24 24"><rect x="1" y="4" width="22" height="19" fill="#fff" stroke="#f26a1f" stroke-width="2"/><rect x="1" y="4" width="22" height="5" fill="#f26a1f"/><path d="M6 1 V6 M18 1 V6" stroke="#f26a1f" stroke-width="2"/><path d="M1 13 H23 M1 18 H23 M8 9 V23 M16 9 V23" stroke="#f26a1f" stroke-width="1"/></svg>
    <div class="panel-title" style="left:44px;top:13px;font-size:12.5px">Hospital Appointments</div>
    <div class="appt" style="top:38px"><div class="date">July<br>16</div><div>Pellentesque accumsan dignissim<br>Wed &nbsp;/ &nbsp; 9:00 am</div></div>
    <div class="appt" style="top:67px"><div class="date">July<br>18</div><div>Pellentesque accumsan dignissim<br>Fri &nbsp; &nbsp;/ &nbsp; 10:00 am</div></div>
  </div>

  <h3 class="abs col-title" style="left:109px">Foot Conditions</h3>
  <ul class="abs list" style="left:90px"><li>Vestibulum</li><li>Eget</li><li>Fringilla</li><li>Odio</li><li>Sed commodo</li><li>Magna pretium</li></ul>
  <ul class="abs list" style="left:206px"><li>Vestibulum</li><li>Eget</li><li>Fringilla</li><li>Odio</li><li>Sed commodo</li><li>Magna pretium</li></ul>

  <h3 class="abs col-title" style="left:381px">Gallery</h3>
  <div class="abs gallery-main" role="img" aria-label="Doctor holding a patient's foot"></div>
  <div class="abs thumb" style="left:364px;width:34px;border:2px solid var(--navy);background:linear-gradient(90deg,#fff,#ead3c2)" role="img" aria-label="Foot examination thumbnail"></div>
  <div class="abs thumb" style="left:401px;width:31px;background:linear-gradient(90deg,#e8d0bc,#c9a77e)" role="img" aria-label="Foot treatment thumbnail"></div>
  <div class="abs thumb" style="left:437px;width:30px;background:linear-gradient(90deg,#3a86c0,#dfe8ef)" role="img" aria-label="Foot care thumbnail"></div>

  <h3 class="abs col-title" style="left:590px">Contact Us</h3>
  <div class="abs field" style="top:967px;height:15px;padding-top:3px">Enter name</div>
  <div class="abs field" style="top:987px;height:15px;padding-top:3px">Enter email address</div>
  <div class="abs field" style="top:1006px;height:48px">Your message</div>
  <div class="abs submit">Submit</div>
</section>

<footer class="abs footer">
  <a href="#" style="left:87px">Home</a>
  <span class="sep" style="left:130px"></span>
  <a href="#" style="left:150px">Appointment</a>
  <span class="sep" style="left:232px"></span>
  <a href="#" style="left:258px">About</a>
  <span class="sep" style="left:306px"></span>
  <a href="#" style="left:323px">Services</a>
  <span class="sep" style="left:379px"></span>
  <a href="#" style="left:398px">Get In Touch</a>
  <div class="copyright">Copyright © 2014. YourCompanyName. All Rights Reserved</div>
  <span class="social" style="left:88px;background:#3b5b99"></span>
  <span class="social" style="left:103px;background:#d62b2b"></span>
  <span class="social" style="left:117px;background:#2aa3e0"></span>
  <div class="address">Seabrook 42 Harbour View Road PO Box<br>3188, Seabrook WA 6000<br>P 08 9000 1234 F 08 9000 1235<br>Ridgemont 7/14 Carrow Street PO Box 20581,</div>
</footer>

</body>
</html>
```